VIP Fashion Nightclub Flyer Design

Lanterns and Keys is set to be a platform for fashion brands, artists and designers to showcase their talents. In the past, launch parties etc. would have had to be organised by the brand itself. Lanterns and Keys aims to provide a direct link with the fashion community.

We need a flyer design for our nightclubs grand opening. We would like to see designs that use mostly black on black. We also would like to create a feeling of luxury and exclusivity. Please see fashion editorials for reference.

See below for flyer text:

Lanterns & Keys
X
Velvet Moth

GRAND OPENING
Sydney’s Most Exclusive Event
SATURDAY 12th OF MAY 2012

General 10PM – LATE
VIP 9PM - LATE

Register today for an invite:
www.glimmerlounge-example.com.au

Live Music and DJ’s

The Brambling Hotel
218 Wexley St
Darlinghurst
Updates

Hi guys, ive added some images like our logo and wax stamps that we use for our personal invitations.

Target Market(s)

Lanterns and Keys targets 20-30 year olds in the fashion industry, models, retailers and designers.

Industry/Entity Type

Fashion

Requirements
Must have
• Must be made into 3 sizes:
A1
Pictogram Cover Art
1000px x 1000px

```html
<!DOCTYPE html>
<html lang="en">
<head>
<meta charset="utf-8">
<title>Lanterns &amp; Keys x Velvet Moth – Grand Opening</title>
<link rel="stylesheet" href="https://fonts.googleapis.com/css2?family=Oswald:wght@500;700&family=Great+Vibes&family=Roboto:wght@400;700&display=swap">
<style>
  :root {
    --paper: #ffffff;
    --night: #05060c;
    --night-blue: #101a3a;
    --haze: #3a4a7a;
    --neon-pink: #ff2ea6;
    --neon-cyan: #27c9f2;
    --text-light: #ffffff;
    --text-dark: #0a1a2a;
  }
  * { margin: 0; padding: 0; box-sizing: border-box; }
  html, body {
    width: 865px; height: 1200px; overflow: hidden;
    background: var(--paper);
  }
  .flyer {
    position: relative;
    width: 865px; height: 1200px;
    background: var(--paper);
  }
  .scene-photo {
    position: absolute;
    left: 23px; top: 23px; right: 23px; bottom: 45px;
    background: radial-gradient(ellipse 70% 55% at 72% 22%, var(--haze) 0%, var(--night-blue) 45%, var(--night) 85%);
  }
  .brand {
    position: absolute; left: 108px; top: 212px;
    white-space: nowrap;
  }
  .brand-host {
    font-family: "Oswald", sans-serif; font-weight: 700;
    font-size: 56px; line-height: 1; color: var(--neon-pink);
    letter-spacing: 1px;
  }
  .brand-cross {
    display: block; width: 58px; height: 58px; margin: 12px 0 6px 66px;
  }
  .brand-guest {
    font-family: "Oswald", sans-serif; font-weight: 700;
    font-size: 84px; line-height: 1; color: var(--neon-cyan);
    margin-left: -8px;
  }
  .headline {
    position: absolute; left: 180px; top: 600px;
    white-space: nowrap;
  }
  .headline-acts {
    font-family: "Oswald", sans-serif; font-weight: 700;
    font-size: 54px; line-height: 1; color: var(--neon-pink);
  }
  .headline-opening {
    font-family: "Great Vibes", cursive; font-weight: 400;
    font-size: 70px; line-height: 1; color: var(--text-light);
    margin: 2px 0 0 112px;
  }
  .details {
    position: absolute; left: 368px; top: 762px; width: 440px;
    font-family: "Roboto", sans-serif; color: var(--text-light);
  }
  .details-tagline, .details-date { font-size: 23px; line-height: 1.3; }
  .details-date { font-weight: 700; }
  .entry { margin-top: 14px; }
  .entry-title {
    font-family: "Oswald", sans-serif; font-weight: 700;
    font-size: 40px; line-height: 1.05;
  }
  .entry-title.vip { color: var(--neon-pink); }
  .entry-title.general { color: var(--neon-cyan); }
  .entry-time { font-size: 25px; line-height: 1.3; }
  .register-bar {
    position: absolute; left: 80px; top: 1035px; width: 705px; height: 34px;
    background: var(--neon-cyan); color: var(--text-dark);
    font-family: "Roboto", sans-serif; font-size: 20px;
    display: flex; align-items: center; justify-content: center;
  }
  .venue-band {
    position: absolute; left: 23px; top: 1078px; width: 819px; height: 77px;
    background: var(--neon-pink); color: var(--text-light);
    font-family: "Roboto", sans-serif; font-size: 30px;
    display: flex; align-items: center; justify-content: center;
  }
</style>
</head>
<body>
  <main class="flyer">
    <div class="scene-photo" role="img" aria-label="Nightclub photograph: a dancer wearing headphones with hair flying, against blurred colourful party lights"></div>

    <header class="brand">
      <div class="brand-host">Lanterns &amp; Keys</div>
      <svg class="brand-cross" viewBox="0 0 58 58" aria-label="x">
        <circle cx="29" cy="29" r="28" fill="#ff2ea6"/>
        <path d="M19 19 L39 39 M39 19 L19 39" stroke="#ffffff" stroke-width="6" stroke-linecap="round"/>
      </svg>
      <div class="brand-guest">Velvet Moth</div>
    </header>

    <section class="headline">
      <h1 class="headline-acts">Live Music and DJ's</h1>
      <h2 class="headline-opening">Grand Opening</h2>
    </section>

    <section class="details">
      <p class="details-tagline">Sydney's Most Exclusive Event</p>
      <p class="details-date">SATURDAY 12th OF MAY 2012</p>
      <div class="entry">
        <h3 class="entry-title vip">VIP ENTRY</h3>
        <p class="entry-time">The Saddle Lounge – 9PM – 4AM</p>
      </div>
      <div class="entry">
        <h3 class="entry-title general">GENERAL ENTRY</h3>
        <p class="entry-time">The Linen Room - 10PM – 4AM</p>
      </div>
    </section>

    <p class="register-bar">Register today for an invite: www.glimmerlounge-example.com.au</p>
    <footer class="venue-band">The Brambling Hotel • 218 Wexley St • Darlinghurst</footer>
  </main>
</body>
</html>
```